Website design for learning and development business

I need a logo for my new business based in Australasia. I am a kiwi who is a creative change maker working in the Learning & development space. I design experiential learning opportunities for businesses to grow and nurture their tribes. I take a holistic look at an organisation and analyse what is needed to build a positive culture with a growth mindset woven into their DNA. I would like to see designs that are based on the following word snaps - creative, interesting, tribal, journey, adaptability, engaging, fluid, architectural, bespoke, courageous, challenging .I have the logo (attached) and I Need a startup business website designed. I am a Learning and development professional who is looking at going out on my own and establishing my own business. I would like a website designed that people would go to to check out what I do, how I do, what skills I have and how to contact me. Also room for a blog/articles.

Target Market(s)

Small to medium business

Industry/Entity Type

Self employed training and consultancy company

Number of Pages Required

5+ page

Requirements
Must have
• home page, about page, contact us page, blog page, search for us page
Nice to have
• Testimonials,

```html
<!DOCTYPE html>
<html lang="en">
<head>
<meta charset="utf-8">
<title>Kaleido Consulting — Learning and Development</title>
<link rel="stylesheet" href="https://fonts.googleapis.com/css2?family=Rubik:wght@500;700;800&family=Poppins:wght@400;500;600&display=swap">
<style>
:root{
  --red:#e3231f;
  --orange:#ee5a2f;
  --green:#46ad35;
  --yellow:#e9d21c;
  --cream:#fdf4ef;
  --ink:#1c1c1c;
  --body:#6a6a6a;
  --card:#f4f4f4;
  --dark:#1d2027;
  --date:#3d7fd8;
  --social:#2f73d6;
}
*{box-sizing:border-box;margin:0;padding:0}
html,body{width:1200px;height:4310px;overflow:hidden}
body{position:relative;font-family:"Poppins",sans-serif;color:var(--ink);background:#fff}
.abs{position:absolute}
.heading{font-family:"Rubik",sans-serif;font-weight:800;letter-spacing:1px}
.section-title{position:absolute;left:0;width:1200px;text-align:center;font-family:"Rubik",sans-serif;font-weight:800;font-size:37px;letter-spacing:1.5px;color:var(--ink)}
.section-lead{position:absolute;left:260px;width:680px;text-align:center;font-size:13px;line-height:27px;color:var(--body)}
.btn{position:absolute;display:flex;align-items:center;justify-content:center;border-radius:24px;color:#fff;font-family:"Poppins",sans-serif;font-weight:600;font-size:13px;letter-spacing:.5px}
.brand{position:absolute;color:#fff;font-family:"Rubik",sans-serif;font-weight:700;line-height:1;text-align:center}
.brand span{display:block}
.brand .brand-main{font-size:27px;letter-spacing:1px}
.brand .brand-sub{font-size:11px;letter-spacing:4px;margin-top:3px}
.placeholder{position:absolute}

/* hero */
.hero{position:absolute;left:0;top:0;width:1200px;height:670px;overflow:hidden}
.hero-photo{position:absolute;inset:0;background:linear-gradient(120deg,#2a2a2c 0%,#1e1f22 45%,#34312e 75%,#222 100%)}
.nav{position:absolute;top:56px;font-size:13px;color:#fff;letter-spacing:.3px}
.nav.active{color:#f2d21a}
.phone-btn{left:952px;top:44px;width:188px;height:43px;background:var(--green);font-size:14px;letter-spacing:.3px}
.phone-btn svg{margin-right:6px}
.hero-title{position:absolute;left:60px;top:190px;font-family:"Rubik",sans-serif;font-weight:700;font-size:47px;line-height:55px;color:#fff;letter-spacing:1px}
.hero-text{position:absolute;left:60px;top:310px;width:520px;font-size:13.5px;line-height:26.5px;color:#fff}
.hero-btn{left:60px;top:412px;width:164px;height:43px;background:var(--red)}

/* about */
.about{position:absolute;left:0;top:670px;width:1200px;height:334px;background:var(--cream)}
.about-title{position:absolute;left:62px;top:72px;font-size:38px;line-height:49px;color:var(--ink)}
.about-btn{left:62px;top:185px;width:164px;height:44px;background:var(--orange)}
.about-text{position:absolute;left:482px;top:77px;width:654px;font-size:13.4px;line-height:26.4px;color:var(--body)}
.about-text p+p{margin-top:26px}

/* services */
.service-card{position:absolute;top:1230px;width:248px;height:406px;background:var(--card)}
.service-photo{width:248px;height:180px}
.service-card h3{margin:20px 16px 0;font-family:"Rubik",sans-serif;font-weight:700;font-size:16px;line-height:26px;letter-spacing:.6px;color:var(--ink)}
.service-card p{margin:12px 18px 0;font-size:11.5px;line-height:22.5px;color:var(--body)}

/* approach */
.approach{position:absolute;left:0;top:1726px;width:1200px;height:713px;overflow:hidden;background:linear-gradient(180deg,#23262e 0%,#1c2029 55%,#252b38 100%)}
.approach .section-title{color:#fff;top:60px}
.approach .section-lead{color:#d8d8d8;top:118px}
.pillar-title{position:absolute;font-family:"Rubik",sans-serif;font-weight:700;font-size:16px;letter-spacing:1px;color:#fff}
.pillar-text{position:absolute;font-size:11.5px;line-height:23px;color:#e6e6e6;width:240px}

/* blog */
.blog-card{position:absolute;top:2658px;width:337px;height:459px;background:var(--card)}
.blog-photo{width:337px;height:224px}
.blog-card h3{margin:20px 19px 0;font-family:"Rubik",sans-serif;font-weight:700;font-size:16px;line-height:27px;letter-spacing:.6px;color:var(--ink)}
.blog-date{margin:6px 19px 0;font-size:10.5px;color:var(--date)}
.blog-card p{margin:12px 19px 0;font-size:11.3px;line-height:22.5px;color:var(--body)}
.read-more{display:flex;align-items:center;margin:14px 19px 0;font-family:"Rubik",sans-serif;font-weight:700;font-size:11.5px;color:var(--red);letter-spacing:.5px}
.read-more svg{margin-left:6px}

/* contact */
.contact{position:absolute;left:0;top:3214px;width:1200px;height:1096px;background:var(--cream)}
.field{position:absolute;background:#fff;border:1px solid #efe7e2;font-size:13px;color:#555;padding:12px 12px}
.send-btn{left:507px;top:452px;width:186px;height:43px;background:var(--orange)}

/* footer */
.footer-head{position:absolute;top:4067px;font-family:"Rubik",sans-serif;font-weight:700;font-size:13px;letter-spacing:1px;color:var(--green)}
.footer-link{position:absolute;left:340px;font-size:12px;color:#fff}
.footer-link.active{color:#f2d21a}
.footer-text{position:absolute;font-size:12px;line-height:20px;color:#fff}
.social{position:absolute;left:894px;display:flex;align-items:center;font-size:12.5px;color:#fff}
.social i{display:block;width:28px;height:28px;border-radius:50%;background:var(--social);margin-right:10px}
.copyright{position:absolute;left:60px;top:4232px;width:240px;font-size:11.5px;line-height:21px;color:#fff}
.copyright b{font-weight:400;color:var(--red)}
</style>
</head>
<body>

<!-- HERO -->
<header class="hero">
  <div class="hero-photo" role="img" aria-label="Photo of a team meeting around a table, dimmed with a dark overlay"></div>
  <div class="brand" style="left:60px;top:58px;width:182px">
    <span class="brand-main">KALEIDO</span>
    <span class="brand-sub">CONSULTING</span>
  </div>
  <span class="nav active" style="left:492px">HOME</span>
  <span class="nav" style="left:564px">ABOUT US</span>
  <span class="nav" style="left:664px">WHAT WE DO</span>
  <span class="nav" style="left:782px">BLOG</span>
  <span class="nav" style="left:850px">CONTACT US</span>
  <div class="btn phone-btn">
    <svg width="15" height="15" viewBox="0 0 24 24" aria-hidden="true"><path fill="#fff" d="M6.6 10.8a15.1 15.1 0 0 0 6.6 6.6l2.2-2.2c.3-.3.7-.4 1-.2 1.1.4 2.3.6 3.6.6.6 0 1 .4 1 1V20c0 .6-.4 1-1 1A17 17 0 0 1 3 4c0-.6.4-1 1-1h3.5c.6 0 1 .4 1 1 0 1.3.2 2.5.6 3.6.1.3 0 .7-.2 1z"/></svg>
    +1 555 010 2040
  </div>
  <h1 class="hero-title">Learning and<br>Developemnt Company</h1>
  <p class="hero-text">Creative change maker working in the Learning &amp; development space. I design experiential learning opportunities for businesses to grow and nurture their tribes.</p>
  <div class="btn hero-btn">GET STARTED</div>
  <svg class="abs" style="left:0;top:0" width="1200" height="670" viewBox="0 0 1200 670" aria-hidden="true">
    <path fill="#fdf4ef" d="M0,662 C180,632 400,680 540,580 C640,505 700,420 820,410 C960,398 1080,520 1200,545 L1200,670 L0,670 Z"/>
  </svg>
  <div class="placeholder" role="img" aria-label="Large brand emblem decoration" style="left:668px;top:330px;width:380px;height:300px;border-radius:50%;background:radial-gradient(ellipse at center,rgba(70,173,53,.28) 0%,rgba(227,35,31,.14) 55%,rgba(253,244,239,0) 72%)"></div>
</header>

<!-- ABOUT -->
<section class="about">
  <h2 class="heading about-title">KALEIDO<br>CONSULTING</h2>
  <div class="btn about-btn">GET STARTED</div>
  <div class="about-text">
    <p>Lorem Ipsum is simply dummy text of the printing and typesetting industry. Lorem Ipsum has been the industry's standard dummy text ever since the 1500s, when an unknown printer took a galley of type and scrambled it to make a type specimen book. It has survived not only five centuries, but also the leap into electronic typesetting, remaining essentially unchanged.</p>
    <p>It was popularised in the 1960s with the release of Letraset sheets containing Lorem Ipsum passages</p>
  </div>
</section>

<!-- WHAT WE DO -->
<h2 class="section-title" style="top:1085px">WHAT WE DO</h2>
<p class="section-lead" style="top:1145px">Lorem Ipsum is simply dummy text of the printing and typesetting industry. Lorem Ipsum has been the industry's standard dummy text ever since the 1500.</p>

<article class="service-card" style="left:60px">
  <div class="service-photo" role="img" aria-label="Photo of a customer service team working at computers" style="background:linear-gradient(135deg,#5b5f66,#b9b8b3 60%,#3f4147)"></div>
  <h3>Customer service<br>training</h3>
  <p>Lorem Ipsum is simply dummy text of the printing and typesetting industry. Lorem Ipsum has been the industry's standard dummy text ever since the 1500.</p>
</article>
<article class="service-card" style="left:338px">
  <div class="service-photo" role="img" aria-label="Photo of a supportive conversation between colleagues" style="background:linear-gradient(135deg,#8a8f96,#d7c28a 55%,#6f665a)"></div>
  <h3>Mental health awareness</h3>
  <p>Lorem Ipsum is simply dummy text of the printing and typesetting industry. Lorem Ipsum has been the industry's standard dummy text ever since the 1500.</p>
</article>
<article class="service-card" style="left:615px">
  <div class="service-photo" role="img" aria-label="Photo of a presenter leading a policy training session" style="background:linear-gradient(135deg,#c9d0d3,#7d8a8c 55%,#3d4446)"></div>
  <h3>Policy training</h3>
  <p>Lorem Ipsum is simply dummy text of the printing and typesetting industry. Lorem Ipsum has been the industry's standard dummy text ever since the 1500.</p>
</article>
<article class="service-card" style="left:892px">
  <div class="service-photo" role="img" aria-label="Photo of a leadership workshop in a brick-walled room" style="background:linear-gradient(135deg,#8f5a44,#d9d4cc 55%,#4b3d36)"></div>
  <h3>Leadership growth</h3>
  <p>Lorem Ipsum is simply dummy text of the printing and typesetting industry. Lorem Ipsum has been the industry's standard dummy text ever since the 1500.</p>
</article>

<!-- HOW WE DO -->
<section class="approach">
  <div class="abs" role="img" aria-label="Dim background photo of a laptop with data charts" style="inset:0;background:radial-gradient(ellipse at 50% 70%,rgba(70,90,120,.35),rgba(0,0,0,0) 60%)"></div>
  <h2 class="section-title">HOW WE DO</h2>
  <p class="section-lead">Lorem Ipsum is simply dummy text of the printing and typesetting industry. Lorem Ipsum has been the industry's standard dummy text ever since the 1500.</p>

  <div class="pillar-title" style="left:0;width:1200px;text-align:center;top:210px">TRUSTED INTELIGENCED</div>
  <p class="pillar-text" style="left:480px;top:238px;text-align:center">Lorem Ipsum is simply dummy text of the printing and typesetting industry.</p>

  <svg class="abs" style="left:0;top:0" width="1200" height="713" viewBox="0 0 1200 713" aria-hidden="true">
    <circle cx="600" cy="644" r="305" fill="none" stroke="var(--green)" stroke-width="2"/>
    <circle cx="600" cy="680" r="255" fill="none" stroke="var(--yellow)" stroke-width="2"/>
    <circle cx="600" cy="340" r="45" fill="var(--orange)"/>
    <g fill="none" stroke="#fff" stroke-width="2" stroke-linecap="round">
      <path d="M584 340a10 10 0 0 1 3-19 13 13 0 0 1 25 2 8 8 0 0 1 0 17z"/>
      <path d="M592 340v10M600 340v14M608 340v10"/>
      <circle cx="592" cy="352" r="2"/><circle cx="600" cy="356" r="2"/><circle cx="608" cy="352" r="2"/>
    </g>
    <circle cx="341" cy="475" r="45" fill="var(--green)"/>
    <g fill="none" stroke="#fff" stroke-width="2" stroke-linecap="round">
      <path d="M331 495h22M334 489h16l-3-12h-10z"/>
      <path d="M338 477v-10h8v10M336 467h12M342 461v-6M339 458h6"/>
    </g>
    <circle cx="859" cy="475" r="45" fill="var(--green)"/>
    <g fill="none" stroke="#fff" stroke-width="2" stroke-linecap="round">
      <path d="M840 495h40"/>
      <path d="M845 495v-10M853 495v-16M861 495v-12M869 495v-22"/>
      <path d="M843 475l12-8 8 5 14-14M872 458h5v5"/>
    </g>
  </svg>

  <div class="placeholder" role="img" aria-label="Large brand emblem decoration" style="left:435px;top:408px;width:352px;height:295px;border-radius:50%;background:radial-gradient(ellipse at center,rgba(70,173,53,.3) 0%,rgba(227,35,31,.15) 50%,rgba(0,0,0,0) 72%)"></div>

  <div class="pillar-title" style="left:38px;width:240px;text-align:right;top:450px">STRATEGY</div>
  <p class="pillar-text" style="left:38px;top:479px;text-align:right">Lorem Ipsum is simply dummy text of the printing and typesetting industry.</p>
  <div class="pillar-title" style="left:921px;top:450px">BUSINESS GROWTH</div>
  <p class="pillar-text" style="left:921px;top:479px">Lorem Ipsum is simply dummy text of the printing and typesetting industry.</p>
</section>

<!-- RECENT BLOG -->
<h2 class="section-title" style="top:2521px">RECENT BLOG</h2>
<p class="section-lead" style="top:2581px">Lorem Ipsum is simply dummy text of the printing and typesetting industry. Lorem Ipsum has been the industry's standard dummy text ever since the 1500.</p>

<article class="blog-card" style="left:60px">
  <div class="blog-photo" role="img" aria-label="Photo of colleagues talking in a bright office" style="background:linear-gradient(135deg,#6d7468,#d1d2c8 50%,#4e5249)"></div>
  <h3>Lorem ipsum is simply dummy text and printing typesetting.</h3>
  <div class="blog-date">27 July 2021</div>
  <p>Lorem Ipsum is simply dummy text of the printing and typesetting industry. Lorem Ipsum has been the industry's standard dummy text ever since the 1500...</p>
  <div class="read-more">READ MORE <svg width="16" height="10" viewBox="0 0 16 10" aria-hidden="true"><path d="M1 5h13M10 1l4 4-4 4" fill="none" stroke="var(--green)" stroke-width="1.5"/></svg></div>
</article>
<article class="blog-card" style="left:432px">
  <div class="blog-photo" role="img" aria-label="Photo of a businessperson with a digital learning graphic" style="background:linear-gradient(135deg,#dfe3e8,#6f8fb6 55%,#203a66)"></div>
  <h3>Lorem ipsum is simply dummy text and printing typesetting.</h3>
  <div class="blog-date">27 July 2021</div>
  <p>Lorem Ipsum is simply dummy text of the printing and typesetting industry. Lorem Ipsum has been the industry's standard dummy text ever since the 1500...</p>
  <div class="read-more">READ MORE <svg width="16" height="10" viewBox="0 0 16 10" aria-hidden="true"><path d="M1 5h13M10 1l4 4-4 4" fill="none" stroke="var(--green)" stroke-width="1.5"/></svg></div>
</article>
<article class="blog-card" style="left:804px">
  <div class="blog-photo" role="img" aria-label="Photo of hands reviewing documents on a desk" style="background:linear-gradient(135deg,#4f6270,#a9a394 55%,#2e3a42)"></div>
  <h3>Lorem ipsum is simply dummy text and printing typesetting.</h3>
  <div class="blog-date">27 July 2021</div>
  <p>Lorem Ipsum is simply dummy text of the printing and typesetting industry. Lorem Ipsum has been the industry's standard dummy text ever since the 1500...</p>
  <div class="read-more">READ MORE <svg width="16" height="10" viewBox="0 0 16 10" aria-hidden="true"><path d="M1 5h13M10 1l4 4-4 4" fill="none" stroke="var(--green)" stroke-width="1.5"/></svg></div>
</article>

<!-- CONTACT + FOOTER -->
<section class="contact">
  <h2 class="section-title" style="top:61px">CONTACT US</h2>
  <p class="section-lead" style="top:122px">Lorem Ipsum is simply dummy text of the printing and typesetting industry. Lorem Ipsum has been the industry's standard dummy text ever since the 1500.</p>
  <div class="field" style="left:270px;top:211px;width:321px;height:43px">Name</div>
  <div class="field" style="left:606px;top:211px;width:323px;height:43px">Contact No.</div>
  <div class="field" style="left:270px;top:271px;width:659px;height:44px">Email</div>
  <div class="field" style="left:270px;top:331px;width:659px;height:104px">Message</div>
  <div class="btn send-btn">SEND MESSAGE</div>
</section>

<footer>
  <svg class="abs" style="left:0;top:3700px" width="1200" height="610" viewBox="0 0 1200 610" aria-hidden="true">
    <defs>
      <linearGradient id="footerShade" x1="0" y1="0" x2="1" y2="1">
        <stop offset="0" stop-color="#2a2825"/>
        <stop offset=".5" stop-color="#1b1c1f"/>
        <stop offset="1" stop-color="#26231f"/>
      </linearGradient>
    </defs>
    <path fill="url(#footerShade)" d="M1200,40 C1050,90 900,110 760,150 C620,190 520,170 450,250 C390,320 330,420 220,420 C140,420 70,405 0,400 L0,610 L1200,610 Z"/>
  </svg>
  <div class="abs" role="img" aria-label="Dim background photo of a smiling professional" style="left:600px;top:3760px;width:600px;height:550px;background:radial-gradient(ellipse at 70% 30%,rgba(120,90,70,.25),rgba(0,0,0,0) 65%)"></div>

  <div class="placeholder" role="img" aria-label="Large brand emblem decoration" style="left:60px;top:3790px;width:410px;height:310px;border-radius:50%;background:radial-gradient(ellipse at center,rgba(70,173,53,.28) 0%,rgba(227,35,31,.13) 52%,rgba(253,244,239,0) 72%)"></div>

  <div class="abs" aria-label="Partner badges" style="left:618px;top:3912px;width:520px;height:36px;display:flex;justify-content:space-between;align-items:center">
    <span style="display:block;width:56px;height:34px;border-radius:50%;background:#2a63b8"></span>
    <span style="display:block;width:110px;height:26px;border-radius:4px;background:#e8e8e8"></span>
    <span style="display:block;width:112px;height:26px;border-radius:4px;background:#4a86e8"></span>
    <span style="display:block;width:130px;height:26px;border-radius:4px;background:#2d6fc4"></span>
  </div>

  <div class="brand" style="left:60px;top:4160px;width:182px">
    <span class="brand-main">KALEIDO</span>
    <span class="brand-sub">CONSULTING</span>
  </div>
  <p class="copyright">© <b>KALEIDO CONSULTING</b> - 2021. All Right Reserved.</p>

  <div class="footer-head" style="left:340px">USEFUL LINKS</div>
  <span class="footer-link active" style="top:4104px">Home</span>
  <span class="footer-link" style="top:4134px">About Us</span>
  <span class="footer-link" style="top:4164px">What we do</span>
  <span class="footer-link" style="top:4194px">Blog</span>
  <span class="footer-link" style="top:4224px">Contact Us</span>

  <div class="footer-head" style="left:618px">CONTACT INFO</div>
  <svg class="abs" style="left:617px;top:4105px" width="12" height="16" viewBox="0 0 12 16" aria-hidden="true"><path fill="var(--red)" d="M6 0a6 6 0 0 0-6 6c0 4.5 6 10 6 10s6-5.5 6-10a6 6 0 0 0-6-6zm0 8.3A2.3 2.3 0 1 1 6 3.7a2.3 2.3 0 0 1 0 4.6z"/></svg>
  <p class="footer-text" style="left:646px;top:4100px;width:230px">Lorem ipsum is simply dummy text and printing and typesetting.</p>
  <svg class="abs" style="left:616px;top:4170px" width="14" height="14" viewBox="0 0 24 24" aria-hidden="true"><path fill="var(--red)" d="M6.6 10.8a15.1 15.1 0 0 0 6.6 6.6l2.2-2.2c.3-.3.7-.4 1-.2 1.1.4 2.3.6 3.6.6.6 0 1 .4 1 1V20c0 .6-.4 1-1 1A17 17 0 0 1 3 4c0-.6.4-1 1-1h3.5c.6 0 1 .4 1 1 0 1.3.2 2.5.6 3.6.1.3 0 .7-.2 1z"/></svg>
  <p class="footer-text" style="left:646px;top:4167px">555 010 2040</p>
  <svg class="abs" style="left:616px;top:4218px" width="14" height="11" viewBox="0 0 14 11" aria-hidden="true"><path fill="var(--red)" d="M0 0h14v11H0z"/><path d="M0 0l7 6 7-6" fill="none" stroke="#1d1d20" stroke-width="1.4"/></svg>
  <p class="footer-text" style="left:646px;top:4213px">hello@kaleidoconsulting.example</p>

  <div class="footer-head" style="left:894px">FOLLOW US</div>
  <div class="social" style="top:4100px"><i></i>Circlebook</div>
  <div class="social" style="top:4145px"><i></i>Chirper</div>
  <div class="social" style="top:4190px"><i></i>Workline</div>
</footer>

</body>
</html>
```